Etiketten für Olivenöl-Intensivcreme
Zielgruppe
Wir produzieren Bio-Food, u.a. Wein und Olivenöl. Jetzt soll eine Olivenöl-Intensivcreme im Bereich Kosmetik auf dem Markt platziert werden. Unsere Zielgruppe hat ein sehr breites Altersspektrum (jung bis alt), ist naturverbunden, tierlieb, gebildet, kritisch-reflektierend, weiß gute Qualität zu schätzen, ist überwiegend weiblich. Die Olivenöl-Intensivcreme hat eine sehr breite Verwendung und soll sich als 'Allzweckwaffe' in jedem Haushalt etablieren (Babyhaut-Pflege, Lippenpflege, Ganzkörperpflege, Hand-Schutzcreme etc.).
Aufgabenstellung
Die Creme soll heißen: Tavunel (es könnte z.B. der Buchstabe 'O' durch eine Olive ersetzt werden). Es gibt zwei Etikette (Deckeloberseite der Metalldose und auf dem Boden). Der Durchmesser der Etikette ist jeweils 5,5 cm. Die Deckelunterseite gilt reinen Pflichtangaben. Im Dateidownloadbereich sind die Textvorgaben für die Etikette. MUT zur Farbe! Wir sind NICHT brav und angepasst! Orange kann Akzente setzen bzw. für Aufmerksamkeit im Regal sorgen.

```html
<!DOCTYPE html>
<html lang="de">
<head>
<meta charset="utf-8">
<title>Tavunel – Olivenöl-Intensivcreme Etikett</title>
<link rel="stylesheet" href="https://fonts.googleapis.com/css2?family=Josefin+Sans:wght@300;400&family=Amatic+SC:wght@700&display=swap">
<style>
  :root {
    --paper: #ffffff;
    --ink: #1c1c1c;
    --orange: #f3974a;
    --orange-soft: #f9c79c;
    --rim: #b9b9b9;
    --rim-light: #e4e4e4;
    --backdrop: #f4f4f4;
  }
  html, body {
    margin: 0;
    padding: 0;
    width: 1200px;
    height: 1160px;
    overflow: hidden;
    background: var(--backdrop);
  }
  .label-canvas {
    display: block;
    width: 1200px;
    height: 1160px;
  }
  .ring-text {
    font-family: "Josefin Sans", sans-serif;
    font-weight: 300;
    font-size: 92px;
    fill: var(--ink);
  }
  .ring-star {
    font-family: "Josefin Sans", sans-serif;
    font-size: 60px;
    fill: var(--ink);
  }
  .producer-name {
    font-family: "Josefin Sans", sans-serif;
    font-weight: 400;
    font-size: 44px;
    fill: var(--ink);
  }
  .product-name {
    font-family: "Josefin Sans", sans-serif;
    font-weight: 300;
    font-size: 150px;
    fill: var(--ink);
  }
  .tag-box { fill: var(--ink); }
  .tag-text {
    font-family: "Amatic SC", sans-serif;
    font-weight: 700;
    fill: var(--paper);
  }
</style>
</head>
<body>
<svg class="label-canvas" viewBox="0 0 1200 1160" xmlns="http://www.w3.org/2000/svg">
  <defs>
    <radialGradient id="spiral-tone" cx="50%" cy="50%" r="50%">
      <stop offset="0%" stop-color="var(--orange-soft)"/>
      <stop offset="55%" stop-color="var(--orange)" stop-opacity="0.85"/>
      <stop offset="100%" stop-color="var(--orange)" stop-opacity="0.55"/>
    </radialGradient>
    <!-- left arc: clockwise, letters face outward -->
    <path id="arc-left" d="M 248 827 A 430 430 0 0 1 453 176"/>
    <!-- bottom + right arc: counter-clockwise, letters face inward -->
    <path id="arc-right" d="M 387 1038 A 505 505 0 1 0 789 112"/>
  </defs>

  <!-- label disc and rim -->
  <circle class="label-rim" cx="600" cy="580" r="548" fill="var(--rim-light)" stroke="var(--rim)" stroke-width="8"/>
  <circle class="label-disc" cx="600" cy="580" r="530" fill="var(--paper)"/>

  <!-- decorative spiral area -->
  <circle class="spiral-field" role="img" aria-label="Orangefarbenes Punktmuster in Spiralform" cx="575" cy="590" r="345" fill="url(#spiral-tone)"/>

  <!-- horse illustration area -->
  <rect class="horse-illustration" role="img" aria-label="Zeichnung eines springenden Pferdes" x="530" y="95" width="82" height="128" rx="10" fill="#d9d9d9"/>

  <!-- circular wording -->
  <text class="ring-text"><textPath href="#arc-left" textLength="780" lengthAdjust="spacing">NATURKOSMETIK</textPath></text>
  <text class="ring-text"><textPath href="#arc-right" textLength="1590" lengthAdjust="spacing">OLIVENÖL-INTENSIVCREME</textPath></text>
  <text class="ring-star" x="330" y="1012">*</text>

  <!-- producer -->
  <text class="producer-name" x="575" y="300" text-anchor="middle">KALMERA.HOF</text>

  <!-- claim tags -->
  <g class="tag tag-bio" transform="rotate(-4 660 400)">
    <rect class="tag-box" x="575" y="360" width="175" height="76"/>
    <text class="tag-text" x="662" y="418" font-size="58" text-anchor="middle">BIO-OLIVE</text>
  </g>
  <g class="tag tag-vegan" transform="rotate(-2 720 485)">
    <rect class="tag-box" x="655" y="448" width="130" height="72"/>
    <text class="tag-text" x="720" y="504" font-size="58" text-anchor="middle">VEGAN</text>
  </g>

  <!-- product name -->
  <circle class="name-dot" cx="262" cy="520" r="20" fill="var(--ink)"/>
  <text class="product-name" x="570" y="668" text-anchor="middle">Tavunel</text>

  <!-- use tags -->
  <g class="tag tag-care" transform="rotate(4 490 780)">
    <rect class="tag-box" x="410" y="742" width="160" height="72"/>
    <text class="tag-text" x="490" y="798" font-size="56" text-anchor="middle">PFLEGE-&amp;</text>
  </g>
  <g class="tag tag-protect" transform="rotate(5 475 852)">
    <rect class="tag-box" x="362" y="816" width="228" height="72"/>
    <text class="tag-text" x="476" y="872" font-size="56" text-anchor="middle">SCHUTZCREME</text>
  </g>
</svg>
</body>
</html>
```